Pale Lanterns True Crime Tour Poster Design

We need an A4 sized poster to promote our weekly true crime tours. This poster will be posted onto community noticeboards.
Lots of information and images can be viewed at the following links:-
www.palelanterns.com.au
www.palelanterns.com.au/bookings/
https://www.facebook.com/palelanternswalks/
https://www.travelnotes.com.au/Attraction_Review-g481736-d27159404-Reviews-Pale_Lanterns-Newcastle_Greater_Newcastle_New_South_Wales.html
There are also a number of images for possible use at the following link - we are open to intepretation:-
http://palelanterns.com.au/tour-photographs/
The font on our website is "SpecialElite" so we would like to continue using that font type.
Target Market(s)
Adults 25-65.
Font styles to use
Other font styles liked:
- Special Elite
Colors
Designer to choose colors to be used in the design.
Look and feel

```html
<!DOCTYPE html>
<html lang="en">
<head>
<meta charset="utf-8">
<title>Pale Lanterns – True Crime Tour</title>
<link rel="stylesheet" href="https://fonts.googleapis.com/css2?family=Special+Elite&family=Montserrat:wght@700&display=swap">
<style>
  :root {
    --panel: #2d121c;
    --ink: #2a1218;
    --red: #e2333d;
    --red-deep: #8f1216;
    --red-soft: #c3262f;
    --banner: #a90f12;
    --highlight: #f6d6e4;
    --mist: #d9e3ee;
    --white: #ffffff;
  }
  html, body {
    margin: 0;
    padding: 0;
    width: 848px;
    height: 1200px;
    overflow: hidden;
    background: #ffffff;
  }
  .poster {
    position: relative;
    width: 848px;
    height: 1200px;
    overflow: hidden;
    font-family: "Special Elite", monospace;
  }
  .poster p, .poster h1 { white-space: nowrap; }
  .side-panel {
    position: absolute;
    left: 0; top: 0;
    width: 265px; height: 1200px;
    background: var(--panel);
  }
  .tour-photo {
    position: absolute;
    left: 265px; top: 0;
    width: 583px; height: 1200px;
    background:
      linear-gradient(200deg, rgba(0,0,0,0) 40%, rgba(20,12,14,0.35) 100%),
      linear-gradient(180deg, #7ea2d6 0%, #92b4de 24%, #5a4a50 31%, #322528 45%, #2a2023 100%);
  }
  .chevron {
    position: absolute;
    left: 0; top: 0;
    width: 848px; height: 1200px;
  }
  .brand {
    position: absolute;
    left: 0; top: 22px;
    width: 265px;
    text-align: center;
  }
  .brand-dot {
    display: block;
    width: 150px; height: 150px;
    margin: 0 auto;
    border-radius: 50%;
    background: var(--red);
  }
  .brand-name {
    display: block;
    margin-top: 14px;
    color: var(--red);
    font-size: 25px;
    letter-spacing: 1px;
    white-space: nowrap;
  }
  .tagline {
    position: absolute;
    left: 288px;
    margin: 0;
    color: var(--ink);
    font-size: 18px;
    letter-spacing: 3.6px;
    font-weight: 700;
  }
  .tagline-top { top: 40px; }
  .tagline-bottom {
    top: 68px;
    padding: 3px 2px 4px;
    background: var(--highlight);
  }
  .whisper {
    position: absolute;
    left: 296px; top: 192px;
    margin: 0;
    color: var(--mist);
    font-size: 14px;
    letter-spacing: 2px;
  }
  .headline {
    position: absolute;
    left: 8px; top: 452px;
    margin: 0;
    color: var(--red);
    font-size: 64px;
    font-weight: 400;
    line-height: 102px;
    letter-spacing: 5px;
  }
  .tour-tag {
    position: absolute;
    left: 10px; top: 667px;
    width: 118px; height: 47px;
    border-radius: 4px;
    background: var(--red-deep);
    color: var(--ink);
    font-size: 38px;
    line-height: 48px;
    text-align: center;
  }
  .claim {
    position: absolute;
    left: 10px; top: 888px;
    margin: 0;
    font-family: "Montserrat", sans-serif;
    font-weight: 700;
    color: var(--red-deep);
    font-size: 16px;
    line-height: 37px;
    letter-spacing: 3px;
  }
  .meeting {
    position: absolute;
    left: 10px; top: 980px;
    margin: 0;
    color: var(--red-soft);
    font-size: 13px;
    line-height: 25.6px;
    letter-spacing: 2px;
  }
  .book-banner {
    position: absolute;
    left: 305px; top: 761px;
    width: 455px; height: 86px;
    background: var(--banner);
    transform: rotate(-15deg);
    transform-origin: center;
    color: var(--white);
  }
  .book-title {
    position: absolute;
    left: 18px; top: 4px;
    margin: 0;
    font-size: 44px;
    line-height: 50px;
    letter-spacing: 14px;
    font-weight: 700;
  }
  .book-line {
    position: absolute;
    left: 40px; top: 52px;
    margin: 0;
    font-size: 21px;
    line-height: 26px;
    letter-spacing: 0.5px;
  }
  .contact {
    position: absolute;
    left: 298px; top: 1046px;
    margin: 0;
    color: var(--red-soft);
    font-size: 18px;
    letter-spacing: 2.6px;
  }
  .contact-title {
    display: block;
    font-size: 20px;
    letter-spacing: 4px;
    margin-bottom: 8px;
  }
  .contact-line {
    display: block;
    line-height: 37px;
    color: #a5202a;
  }
</style>
</head>
<body>
<main class="poster">
  <div class="side-panel"></div>
  <div class="tour-photo" role="img" aria-label="Photograph looking up at a dark brick tower with small windows against a pale blue sky"></div>

  <svg class="chevron" viewBox="0 0 848 1200" aria-hidden="true">
    <polygon fill="#2d121c" points="264,1180 496,800 716,1200 576,1200 480,1064 384,1200 264,1200"/>
  </svg>

  <div class="brand">
    <span class="brand-dot" aria-hidden="true"></span>
    <span class="brand-name">PALE LANTERNS</span>
  </div>

  <p class="tagline tagline-top">TAKE A WALK ON THE DARK SIDE</p>
  <p class="tagline tagline-bottom">REVISIT THE SCENES OF THE CRIMES.</p>
  <p class="whisper">.......stories the city tried to forget.......</p>

  <h1 class="headline">TRUE<br>CRIME</h1>
  <div class="tour-tag">Tour</div>

  <p class="claim">100% TRUE -<br>100% UNBELIEVABLE</p>

  <p class="meeting">Meets at the corner of<br>Harbour St &amp; Quarry St,<br>Newcastle;<br>adjacent to Tide House<br>and the Old Timber<br>Yard. Bring comfortable<br>shoes.</p>

  <div class="book-banner">
    <p class="book-title">BOOK NOW</p>
    <p class="book-line">it'd be a crime to miss out</p>
  </div>

  <p class="contact">
    <span class="contact-title">CONTACT US</span>
    <span class="contact-line">Phone: 0491570156</span>
    <span class="contact-line">Email: info@palelanterns.com.au</span>
    <span class="contact-line">Website: http://palelanterns.com.au</span>
  </p>
</main>
</body>
</html>
```